Dröm website

I need a website that I can talk about the company, mission statement and my background on a page. I need a section where customers can order eqipment , pay for it and be able to search for equipment by brand name or model number, schedule an appointment with the tech and a page for general information such as any promotions I'm having, tips on getting good sleep and developing technology news or updates in sleep medicine. I would like a quick link to facebook and twitter. I will also need a way to upload instructional videos.
Updates

Please check out www.RestaloGear.com for ideas. This is a company like the one I have except I am not all online like they are. I see clients face to face also. I also chose coded but the brief did not save that choice. The website should be coded. Added Monday, June 20, 2016

Target Market(s)

Clients with sleep disorders, need a home sleep study done, who have been denied by insurance or have a large insurance deductible and clients who need an option for a payment plan. Clients age 35-70. Physicians offices and other medical professionals.

Coding

Coded - Design and coding required

Number of Pages Required

5+ page

Font styles to use
Other font styles liked:
• Leave it up to the designer

Requirements
Must have
• User friendly, easy to read lettering, able to put pictures on the website, able to update often, secure payment for supplies, credit card only, able to upload videos, my contact information, "contact me" link, my logo and business name.
Nice to have
• A changing information banner on 1st page to highlight and link to any specials promotions or sales or news.
Should not have
• No cartoon animation,

```html
<!DOCTYPE html>
<html lang="en">
<head>
<meta charset="utf-8">
<title>Dröm – Sleep Care</title>
<link href="https://fonts.googleapis.com/css2?family=Open+Sans:wght@400;600&family=Roboto+Condensed:wght@700&family=Roboto:wght@400;500;700&display=swap" rel="stylesheet">
<style>
:root{
  --navy:#0b4a78;
  --nav-top:#1667a0;
  --nav-bottom:#0a4f80;
  --green:#8cc168;
  --section-blue:#1d5b87;
  --text:#333a40;
  --muted:#6d747a;
  --footer:#1c1e22;
  --white:#ffffff;
  --line:#e4e6e8;
}
*{margin:0;padding:0;box-sizing:border-box}
html,body{width:1200px;height:2532px;overflow:hidden}
body{position:relative;font-family:"Open Sans",Arial,sans-serif;color:var(--text);background:var(--white)}
.abs{position:absolute}
a{color:inherit;text-decoration:none}

/* header */
.site-header{left:0;top:0;width:1200px;height:132px;background:var(--white)}
.brand{display:flex;align-items:center;gap:14px}
.brand-dot{width:70px;height:70px;border-radius:50%;background:var(--green)}
.brand-name{font-family:"Roboto",sans-serif;font-weight:700;font-size:44px;color:var(--navy)}
.header-brand{left:98px;top:30px}
.contact-line{left:622px;top:42px;display:flex;gap:14px;font-family:"Roboto",sans-serif;font-size:14px;color:#555;line-height:23px}
.contact-icon{width:34px;height:34px;border:1px solid #c9dcc0;border-radius:50%;display:flex;align-items:center;justify-content:center;margin-top:6px}
.appt-btn{left:886px;top:46px;width:214px;height:37px;background:var(--navy);color:var(--white);font-family:"Roboto",sans-serif;font-weight:500;font-size:13px;display:flex;align-items:center;justify-content:center;border-radius:2px}

/* nav */
.main-nav{left:0;top:132px;width:1200px;height:52px;background:linear-gradient(var(--nav-top),var(--nav-bottom))}
.main-nav a{position:absolute;top:0;height:52px;line-height:52px;color:var(--white);font-family:"Roboto",sans-serif;font-weight:500;font-size:13px}
.main-nav a.active{background:var(--green);padding:0 24px;left:98px}

/* hero */
.hero{left:0;top:184px;width:1200px;height:545px;overflow:hidden}
.hero-photo{position:absolute;inset:0;background:linear-gradient(100deg,#c7cdd6 0%,#e8e4e0 35%,#d9c3b0 60%,#eceae8 100%)}
.hero-wave{position:absolute;left:0;bottom:0}
.hero-title{left:98px;top:212px;font-family:"Roboto Condensed",sans-serif;font-weight:700;font-size:39px;color:var(--white);text-shadow:0 2px 4px rgba(0,0,0,.35)}
.hero-text{left:98px;top:266px;width:350px;font-size:12px;line-height:19px;color:var(--white)}
.hero-btn{left:98px;top:321px;width:153px;height:40px;background:var(--navy);color:var(--white);font-family:"Roboto",sans-serif;font-weight:500;font-size:15px;display:flex;align-items:center;justify-content:center;gap:9px;border-radius:3px}
.hero-dots{left:98px;top:390px;display:flex;gap:7px;align-items:center}
.hero-dots span{width:11px;height:11px;border-radius:50%;background:#444}
.hero-dots span.on{width:16px;height:16px;background:var(--white);border:2px solid #aaa}

/* disorders */
.section-title{font-family:"Roboto",sans-serif;font-weight:400;font-size:31px;color:#222}
.disorders-title{left:0;top:776px;width:1200px;text-align:center}
.disorder{top:858px;width:240px;text-align:center}
.disorder-photo{width:158px;height:158px;border-radius:50%;margin:0 auto;border:2px solid var(--navy);padding:4px;background-clip:content-box}
.disorder h3{font-family:"Roboto",sans-serif;font-weight:400;font-size:19px;color:#444;margin-top:22px}
.disorder p{font-size:11.5px;line-height:20px;color:var(--muted);margin-top:12px}

/* video */
.video-band{left:0;top:1183px;width:1200px;height:454px;background:var(--section-blue)}
.video-title{left:98px;top:1264px;font-family:"Roboto Condensed",sans-serif;font-weight:700;font-size:36px;color:var(--white)}
.video-lead{left:98px;top:1320px;width:420px;font-family:"Roboto",sans-serif;font-weight:500;font-size:15.5px;line-height:24px;color:var(--white)}
.video-body{left:98px;top:1386px;width:452px;font-size:12.5px;line-height:22px;color:#e2ebf2}
.video-btn{left:98px;top:1500px;width:147px;height:43px;background:var(--green);color:var(--white);font-family:"Roboto",sans-serif;font-weight:500;font-size:13px;display:flex;align-items:center;justify-content:center;gap:9px;border-radius:2px}
.player{left:606px;top:1257px;width:496px;height:301px;background:var(--white);padding:7px;box-shadow:0 18px 24px rgba(0,0,0,.3)}
.player-screen{width:482px;height:256px;background:linear-gradient(135deg,#3a2e2a,#6b5c58 45%,#1f2530);position:relative}
.play{position:absolute;left:210px;top:98px;width:58px;height:58px;border-radius:50%;border:2px solid rgba(255,255,255,.6);background:rgba(0,0,0,.35)}
.player-bar{height:30px;display:flex;align-items:center;gap:10px;padding:0 6px;font-size:8px;color:#555}
.track{height:3px;background:#ccc;flex:1;position:relative}
.track i{position:absolute;left:0;top:0;height:3px;width:45%;background:#e0532b}
.vol{width:40px;height:3px;background:#e0532b}

/* products */
.products-title{left:127px;top:1682px}
.search{left:822px;top:1688px;display:flex;align-items:center;gap:10px;font-size:15px;color:#555}
.search-select{width:88px;height:30px;border:1px solid #ccc;border-radius:3px;display:flex;align-items:center;justify-content:space-between;padding:0 10px;font-size:15px;color:#444}
.card{top:1767px;width:296px;height:326px;background:#fafafa;border:1px solid var(--line);box-shadow:0 16px 14px -12px rgba(0,0,0,.35);text-align:center}
.card-photo{width:230px;height:190px;margin:20px auto 0;background:linear-gradient(#f3f4f5,#dfe2e5)}
.card p{font-size:12px;line-height:19px;color:#666;margin-top:22px}
.pay-btn{display:inline-block;margin-top:9px;width:102px;height:31px;line-height:31px;background:var(--navy);color:var(--white);font-family:"Roboto",sans-serif;font-weight:500;font-size:11px;border-radius:16px}

/* footer */
.footer-wave{left:0;top:2160px}
.footer{left:0;top:2200px;width:1200px;height:278px;background:var(--footer);color:var(--white)}
.footer-brand{left:98px;top:2228px}
.footer-brand .brand-name{color:var(--white)}
.footer-info{left:98px;top:2318px;font-size:12.5px;line-height:22px;color:#e5e5e5}
.footer-info li{list-style:none;display:flex;gap:16px;margin-bottom:12px;align-items:flex-start}
.footer-h{font-family:"Roboto",sans-serif;font-weight:400;font-size:15.5px;color:var(--white)}
.quick{left:392px;top:2256px}
.quick ul{margin-top:20px;list-style:none;font-size:12.5px;line-height:24px;color:#e5e5e5}
.hours{left:598px;top:2256px}
.hours table{margin-top:18px;font-size:12.5px;color:#e5e5e5;border-collapse:collapse}
.hours td{height:29px;padding-right:26px}
.social{display:flex;gap:6px;margin-top:10px}
.social span{width:22px;height:22px;border:1px solid #bbb;border-radius:50%}
.newsletter{left:854px;top:2256px;width:246px}
.newsletter p{font-size:11.5px;line-height:19px;color:#e5e5e5;margin-top:14px}
.news-input{margin-top:22px;height:41px;background:var(--white);color:#555;font-size:11px;line-height:41px;padding-left:14px}
.subscribe{margin-top:14px;width:102px;height:41px;line-height:41px;text-align:center;background:var(--green);font-family:"Roboto",sans-serif;font-size:12px}
.copyright{left:0;top:2478px;width:1200px;height:54px;background:var(--green);color:var(--white);font-size:12px;text-align:center;line-height:54px}
</style>
</head>
<body>

<header class="site-header abs">
  <div class="brand header-brand abs"><span class="brand-dot"></span><span class="brand-name">Dröm</span></div>
  <div class="contact-line abs">
    <span class="contact-icon"><svg width="16" height="16" viewBox="0 0 24 24"><path d="M6.6 10.8a15 15 0 0 0 6.6 6.6l2.2-2.2a1 1 0 0 1 1-.25 11 11 0 0 0 3.6.6 1 1 0 0 1 1 1V20a1 1 0 0 1-1 1A17 17 0 0 1 3 4a1 1 0 0 1 1-1h3.5a1 1 0 0 1 1 1 11 11 0 0 0 .6 3.6 1 1 0 0 1-.25 1z" fill="#8cc168"/></svg></span>
    <div>Call Us : +1 555 - 210 - 3388<br>hello@drom-sleep.com</div>
  </div>
  <a class="appt-btn abs" href="#">SCHEDULE AN APPOINTMENT</a>
</header>

<nav class="main-nav abs">
  <a class="active" href="#">HOME</a>
  <a style="left:214px" href="#">ABOUT DRÖM</a>
  <a style="left:339px" href="#">SERVICES</a>
  <a style="left:447px" href="#">TREATMENTS</a>
  <a style="left:582px" href="#">SLEEP DISORDERS</a>
  <a style="left:748px" href="#">FINANCING</a>
  <a style="left:868px" href="#">TESTIMONIALS</a>
  <a style="left:1011px" href="#">CONTACT US</a>
</nav>

<section class="hero abs">
  <div class="hero-photo" role="img" aria-label="Photo of a woman kept awake in bed by her partner's snoring, alarm clock beside them"></div>
  <svg class="hero-wave" width="1200" height="70" viewBox="0 0 1200 70"><path d="M0 22 C300 75 700 5 1200 34 L1200 70 L0 70Z" fill="#ffffff"/><path d="M0 22 C300 75 700 5 1200 34" fill="none" stroke="#c9ced3" stroke-width="2"/></svg>
</section>
<h1 class="hero-title abs">SLEEP DISORDERS</h1>
<p class="hero-text abs">Lorem ipsum dolor sit amet, consectetuer adipiscing elit, sed nonummy nibh euismod tincidunt ut laoreet dolore</p>
<a class="hero-btn abs" href="#">MORE INFOR <svg width="14" height="14" viewBox="0 0 14 14"><circle cx="7" cy="7" r="7" fill="#fff"/><path d="M5.5 4l3 3-3 3" stroke="#0b4a78" stroke-width="1.8" fill="none"/></svg></a>
<div class="hero-dots abs"><span class="on"></span><span></span><span></span><span></span></div>

<h2 class="section-title disorders-title abs">SLEEP DISORDERS</h2>
<div class="disorder abs" style="left:81px"><div class="disorder-photo" role="img" aria-label="Photo of a man sleeping with his mouth open" style="background-color:#8a97a6"></div><h3>Sleep Apnea</h3><p>Sed ut perspiciatis unde omnis iste<br>natus error sit voluptatem accusantium<br>doloremque laudantium, totam</p></div>
<div class="disorder abs" style="left:346px"><div class="disorder-photo" role="img" aria-label="Photo of a couple in bed, one snoring" style="background-color:#d9c6b5"></div><h3>Snoring</h3><p>Sed ut perspiciatis unde omnis iste<br>natus error sit voluptatem accusantium<br>doloremque laudantium, totam</p></div>
<div class="disorder abs" style="left:613px"><div class="disorder-photo" role="img" aria-label="Photo of a restless woman lying awake in bed" style="background-color:#c9b09a"></div><h3>Restless leg syndrome</h3><p>Sed ut perspiciatis unde omnis iste<br>natus error sit voluptatem accusantium<br>doloremque laudantium, totam</p></div>
<div class="disorder abs" style="left:878px"><div class="disorder-photo" role="img" aria-label="Photo of a tired man yawning at the office" style="background-color:#9fb0c0"></div><h3>Narcolepsy</h3><p>Sed ut perspiciatis unde omnis iste<br>natus error sit voluptatem accusantium<br>doloremque laudantium, totam</p></div>

<section class="video-band abs" role="img" aria-label="Faded background photo of a person stretching after waking"></section>
<h2 class="video-title abs">INSTRUCTIONAL VIDEO</h2>
<p class="video-lead abs">Nemo enim ipsam voluptatem quia voluptas sit aspernatur aut odit aut fugit, sed quia consequuntur</p>
<p class="video-body abs">Sed ut perspiciatis unde omnis iste natus error sit voluptatem accusantium doloremque laudantium, totam rem aperiam, eaque ipsa quae ab illo inventore veritatis et quasi architecto beatae vitae dicta sunt explicabo. Nemo enim ipsam voluptatem quia voluptas sit aspernatur aut odit aut fugit.</p>
<a class="video-btn abs" href="#">MORE VIDEOS <svg width="13" height="13" viewBox="0 0 14 14"><circle cx="7" cy="7" r="7" fill="#fff"/><path d="M5.5 4l3 3-3 3" stroke="#8cc168" stroke-width="1.8" fill="none"/></svg></a>
<div class="player abs">
  <div class="player-screen" role="img" aria-label="Video still of an older couple sleeping, one wearing a CPAP mask"><span class="play"><svg width="54" height="54" viewBox="0 0 54 54"><path d="M22 17l16 10-16 10z" fill="#fff" opacity=".8"/></svg></span></div>
  <div class="player-bar"><svg width="8" height="8" viewBox="0 0 8 8"><path d="M1 0l6 4-6 4z" fill="#333"/></svg><span>03:00/05:03</span><span class="track"><i></i></span><svg width="10" height="8" viewBox="0 0 10 8"><path d="M0 3h2l3-3v8L2 5H0z" fill="#333"/></svg><span class="vol"></span></div>
</div>

<h2 class="section-title products-title abs">OUR PRODUCTS</h2>
<div class="search abs">Search for Equipment <span class="search-select">brand <svg width="9" height="6" viewBox="0 0 9 6"><path d="M1 1l3.5 3.5L8 1" stroke="#555" fill="none" stroke-width="1.4"/></svg></span></div>
<div class="card abs" style="left:127px"><div class="card-photo" role="img" aria-label="Product photo of a CPAP machine with mask and tubing"></div><p>Ut nisi erat fermentum vel congue<br>id euismod in elit Fusce</p><a class="pay-btn" href="#">PAY NOW</a></div>
<div class="card abs" style="left:452px"><div class="card-photo" role="img" aria-label="Product image of a portable CPAP unit with hose"></div><p>Ut nisi erat fermentum vel congue<br>id euismod in elit Fusce</p><a class="pay-btn" href="#">PAY NOW</a></div>
<div class="card abs" style="left:778px"><div class="card-photo" role="img" aria-label="Product photo of a sleep therapy device with mask"></div><p>Ut nisi erat fermentum vel congue<br>id euismod in elit Fusce</p><a class="pay-btn" href="#">PAY NOW</a></div>

<svg class="footer-wave abs" width="1200" height="44" viewBox="0 0 1200 44"><path d="M0 34 C350 -4 800 -2 1200 36 L1200 44 L0 44Z" fill="#1c1e22"/><path d="M0 34 C350 -4 800 -2 1200 36" fill="none" stroke="#c9ced3" stroke-width="2"/></svg>
<footer class="footer abs"></footer>
<div class="brand footer-brand abs"><span class="brand-dot"></span><span class="brand-name">Dröm</span></div>
<ul class="footer-info abs">
  <li><svg width="14" height="20" viewBox="0 0 14 20"><path d="M7 1a6 6 0 0 0-6 6c0 4.5 6 12 6 12s6-7.5 6-12a6 6 0 0 0-6-6z" fill="none" stroke="#fff" stroke-width="1.5"/><circle cx="7" cy="7" r="2" fill="#fff"/></svg><span>14 Lindell Row, Harbor Vale,<br>4410, Westmere</span></li>
  <li><svg width="16" height="16" viewBox="0 0 24 24"><path d="M6.6 10.8a15 15 0 0 0 6.6 6.6l2.2-2.2a1 1 0 0 1 1-.25 11 11 0 0 0 3.6.6 1 1 0 0 1 1 1V20a1 1 0 0 1-1 1A17 17 0 0 1 3 4a1 1 0 0 1 1-1h3.5a1 1 0 0 1 1 1 11 11 0 0 0 .6 3.6 1 1 0 0 1-.25 1z" fill="none" stroke="#fff" stroke-width="1.6"/></svg><span>Phone : +0215550192</span></li>
  <li><svg width="18" height="14" viewBox="0 0 18 14"><rect x="1" y="1" width="16" height="12" fill="none" stroke="#fff" stroke-width="1.4"/><path d="M1 1l8 7 8-7" fill="none" stroke="#fff" stroke-width="1.4"/></svg><span>Email : care@drom-sleep.com</span></li>
</ul>
<div class="quick abs"><h4 class="footer-h">QUICK LINKS</h4><ul><li>Home</li><li>Snoring &amp; Sleep Apnea</li><li>Treatments</li><li>About Us</li><li>Testimonials</li><li>Contact Us</li></ul></div>
<div class="hours abs"><h4 class="footer-h">BUSINESS HOURS</h4>
  <table><tr><td>Tuesday</td><td>9:00am — 6:00pm</td></tr><tr><td>Wednesday</td><td>9:00am — 6:00pm</td></tr><tr><td>Thursday</td><td>9:00am — 6:00pm</td></tr></table>
  <div class="social" aria-label="Social links"><span></span><span></span><span></span><span></span></div>
</div>
<div class="newsletter abs"><h4 class="footer-h">JOIN OUR NEWSLETTER</h4><p>Excepteur sint occaecat cupidatat non proident, sunt in culpa qui</p><div class="news-input">Enter Name</div><div class="subscribe">SUBSCRIBE</div></div>
<div class="copyright abs">Copyright 2016 | All Rights Reserved – Dröm</div>

</body>
</html>
```